Kiosk Coin Venture: Safe and Secure Cash Money

Front of card: LOGO

Back of card:
$$$ FREE ATM PLACEMENT $$$
BENIFITS OF HAVING AN ATM AT YOUR BUSINESS
FREE ATM and BTM (Bitcoin) installation, maintenance, and loading.
Lower card processing fees
Stimulate more traffic.
Ease of access for customers
Maintain customers inside location.
Higher tips and spending

Contact me for more information!
Name: Tomas Redilla
Phone: (555) 318-7742 - Call or Text
Email: Tomas@VaultLinkpay.example

Contact Information for Business Card

The card should be shape of the logo. Only the back will have all the contact and business details.

Requirements
Must have
• The logo itself will be one side, the card will be the shape of the logo. contact details on back side.

```html
<!DOCTYPE html>
<html lang="en">
<head>
<meta charset="utf-8">
<title>Kiosk Coin Venture – Business Card</title>
<link rel="stylesheet" href="https://fonts.googleapis.com/css2?family=Oswald:wght@500;700&family=Montserrat:wght@400;700&display=swap">
<style>
  :root {
    --bg: #2b2b2b;
    --card: #ffffff;
    --ink: #111111;
    --ink-soft: #3a3a3a;
    --band: #0c0c0c;
    --band-text: #ffffff;
    --rule: #222222;
  }
  * { box-sizing: border-box; margin: 0; padding: 0; }
  html, body {
    width: 1200px; height: 904px; overflow: hidden;
    background: var(--bg);
  }
  .canvas { position: relative; width: 1200px; height: 904px; }

  .card {
    position: absolute;
    width: 580px; height: 331px;
    background: var(--card);
    box-shadow: 0 10px 30px rgba(0,0,0,.45);
    overflow: hidden;
  }

  /* Offer side */
  .card--offer { left: 60px; top: 90px; }
  .offer__headline {
    font-family: "Oswald", sans-serif;
    font-weight: 700;
    font-size: 40px;
    letter-spacing: .5px;
    color: var(--ink);
    text-align: center;
    white-space: nowrap;
    padding-top: 22px;
    line-height: 1.1;
  }
  .offer__band {
    margin-top: 18px;
    background: var(--band);
    color: var(--band-text);
    font-family: "Oswald", sans-serif;
    font-weight: 700;
    font-size: 25px;
    text-align: center;
    white-space: nowrap;
    padding: 7px 0 8px;
    letter-spacing: .5px;
  }
  .offer__benefits {
    display: flex;
    gap: 24px;
    padding: 16px 30px 0 30px;
  }
  .benefit-list {
    list-style: none;
    font-family: "Oswald", sans-serif;
    font-weight: 500;
    font-size: 15px;
    text-transform: uppercase;
    color: var(--ink);
    line-height: 1.4;
  }
  .benefit-list--left { flex: 1.15; }
  .benefit-list--right { flex: 1; }
  .benefit-list li { position: relative; padding-left: 14px; }
  .benefit-list li::before {
    content: "";
    position: absolute; left: 0; top: 9px;
    width: 5px; height: 5px; border-radius: 50%;
    background: var(--ink);
  }

  /* Contact side */
  .card--contact { left: 560px; top: 480px; }
  .brand {
    position: absolute; right: 36px; top: 44px;
    display: flex; align-items: center; gap: 10px;
    font-family: "Montserrat", sans-serif;
    font-weight: 700;
    font-size: 20px;
    color: var(--ink);
  }
  .brand__square { width: 22px; height: 22px; background: var(--ink); }
  .brand-rule {
    position: absolute; left: 300px; right: 36px; top: 118px;
    height: 1.5px; background: var(--rule);
  }
  .contact {
    position: absolute; left: 44px; top: 160px;
    font-family: "Montserrat", sans-serif;
    color: var(--ink);
  }
  .contact__name { font-weight: 700; font-size: 26px; line-height: 1.2; }
  .contact__title { font-size: 15px; color: var(--ink-soft); margin-top: 2px; }
  .contact__rule { width: 250px; height: 1.5px; background: var(--rule); margin: 10px 0 6px; }
  .contact__row {
    display: flex; align-items: center; gap: 12px;
    font-size: 15.5px; line-height: 1.7;
  }
  .contact__icon { width: 14px; height: 14px; flex: none; }
</style>
</head>
<body>
<main class="canvas">

  <section class="card card--offer" aria-label="Offer side">
    <h1 class="offer__headline">$$$ FREE ATM PLACEMENT $$$</h1>
    <div class="offer__band">BENIFITS OF HAVING AN ATM AT YOUR BUSINESS</div>
    <div class="offer__benefits">
      <ul class="benefit-list benefit-list--left">
        <li>Free ATM and BTM (Bitcoin) installation, maintenance, and loading.</li>
        <li>Lower card processing fees</li>
        <li>Stimulate more traffic.</li>
      </ul>
      <ul class="benefit-list benefit-list--right">
        <li>Ease of access for customers</li>
        <li>Maintain customers inside location.</li>
        <li>Higher tips and spending</li>
      </ul>
    </div>
  </section>

  <section class="card card--contact" aria-label="Contact side">
    <div class="brand">
      <span class="brand__square"></span>
      <span class="brand__name">Kiosk Coin Venture</span>
    </div>
    <div class="brand-rule"></div>

    <div class="contact">
      <div class="contact__name">Tomas Redilla</div>
      <div class="contact__title">Managing Director</div>
      <div class="contact__rule"></div>
      <div class="contact__row">
        <svg class="contact__icon" viewBox="0 0 24 24" aria-hidden="true"><path fill="#111" d="M6.6 10.8a15.1 15.1 0 0 0 6.6 6.6l2.2-2.2c.3-.3.7-.4 1-.2 1.1.4 2.3.6 3.6.6.6 0 1 .4 1 1V20c0 .6-.4 1-1 1A17 17 0 0 1 3 4c0-.6.4-1 1-1h3.5c.6 0 1 .4 1 1 0 1.3.2 2.5.6 3.6.1.3 0 .7-.2 1z"/></svg>
        <span>(555) 318-7742 - Call or Text</span>
      </div>
      <div class="contact__row">
        <svg class="contact__icon" viewBox="0 0 24 24" aria-hidden="true"><path fill="#111" d="M2 5h20v14H2z"/><path fill="none" stroke="#fff" stroke-width="1.6" d="M2.5 5.5 12 13l9.5-7.5"/></svg>
        <span>Tomas@VaultLinkpay.example</span>
      </div>
      <div class="contact__row">
        <svg class="contact__icon" viewBox="0 0 24 24" aria-hidden="true"><circle cx="12" cy="12" r="10" fill="#111"/><path fill="none" stroke="#fff" stroke-width="1.4" d="M2 12h20M12 2c3 3 3 17 0 20M12 2c-3 3-3 17 0 20"/></svg>
        <span>www.kioskcoinsite.example</span>
      </div>
    </div>
  </section>

</main>
</body>
</html>
```